Personal training studio poster / postcard

We need a poster / postcard design to advertise our recently established personal training studio - details and logo in the attached file. Logo file also provided.

We are flexible on format. Prefer the use of pictures in the design.

Training

```html
<!DOCTYPE html>
<html lang="en">
<head>
<meta charset="utf-8">
<title>Harwood Strength Studio – Poster</title>
<link rel="stylesheet" href="https://fonts.googleapis.com/css2?family=Oswald:wght@300;400;500&family=Pathway+Gothic+One&display=swap">
<style>
  :root {
    --bg: #000000;
    --white: #ffffff;
    --grey-text: #c8c8c8;
    --silver: #d9d9d9;
    --ink: #2a2a2a;
    --disc-light: #ffffff;
    --disc-edge: #b9b9b9;
    --ring-dark: #4a4a4a;
    --ring-light: #eeeeee;
    --label-top: #4a4a4a;
    --label-bottom: #2e2e2e;
    --icon-yoga: #7a7a7a;
    --icon-mma: #8a8a8a;
    --icon-strength: #6e6e6e;
    --icon-body: #2f6fc4;
    --icon-nutrition: #5aa832;
    --icon-osteo: #c8231f;
  }
  * { margin: 0; padding: 0; box-sizing: border-box; }
  html, body { width: 1200px; height: 850px; overflow: hidden; background: var(--bg); }
  .poster {
    position: relative; width: 1200px; height: 850px; overflow: hidden;
    background: var(--bg);
    font-family: "Pathway Gothic One", sans-serif;
    color: var(--white);
  }
  .backdrop { position: absolute; inset: 0; }

  .studio-name {
    position: absolute; top: 100px; left: 0; width: 1200px; text-align: center;
    font-weight: 400; font-size: 62px; letter-spacing: 4px; color: var(--silver);
    text-transform: uppercase; line-height: 1;
  }
  .tagline {
    position: absolute; top: 236px; left: 0; width: 1200px; text-align: center;
    font-size: 28px; line-height: 32px; color: var(--grey-text);
  }

  .services { position: absolute; left: 86px; top: 284px; }
  .services-title { font-weight: 400; font-size: 46px; line-height: 50px; margin-bottom: 16px; }
  .services-sub { font-size: 29px; line-height: 32px; color: var(--grey-text); }

  .class-list { list-style: none; position: absolute; left: 86px; top: 427px; }
  .class-item { display: flex; align-items: center; height: 44px; margin-bottom: 21.3px; }
  .class-icon {
    width: 43px; height: 43px; border-radius: 50%; flex: none;
    border: 2px solid #dcdcdc; margin-right: 18px;
  }
  .class-icon.yoga { background: var(--icon-yoga); }
  .class-icon.mma { background: var(--icon-mma); }
  .class-icon.strength { background: var(--icon-strength); }
  .class-icon.body { background: var(--icon-body); }
  .class-icon.nutrition { background: var(--icon-nutrition); }
  .class-icon.osteo { background: var(--icon-osteo); }
  .class-label {
    background: linear-gradient(to bottom, var(--label-top), var(--label-bottom));
    font-size: 32px; line-height: 37px; padding: 0 8px 0 4px;
  }

  .disc {
    position: absolute; border-radius: 50%;
    background: radial-gradient(circle at 50% 35%, var(--ring-light), #9a9a9a 55%, var(--ring-dark) 100%);
    box-shadow: 0 0 20px rgba(0,0,0,0.8);
  }
  .disc-face {
    position: absolute; inset: 26px; border-radius: 50%;
    background: radial-gradient(circle at 50% 40%, var(--disc-light) 45%, #e6e6e6 75%, var(--disc-edge) 100%);
    box-shadow: inset 0 0 10px rgba(0,0,0,0.35);
    display: flex; flex-direction: column; align-items: center;
    text-align: center; color: var(--ink);
  }

  .offer-disc { left: 483px; top: 316px; width: 330px; height: 330px; }
  .offer-disc .disc-face { padding-top: 68px; }
  .offer-title { font-size: 46px; line-height: 50px; }
  .offer-line { font-family: "Oswald", sans-serif; font-weight: 300; font-size: 29px; line-height: 38px; }
  .offer-line.first { margin-top: 10px; }
  .offer-line.second { margin-top: 8px; }
  .offer-price { font-weight: 500; }
  .offer-shoes {
    width: 143px; height: 48px; margin-top: 25px; border-radius: 50% / 60%;
    background: linear-gradient(to bottom, #e3e3e3, #a9a9a9);
  }

  .booking-disc { left: 812px; top: 423px; width: 354px; height: 354px; }
  .booking-disc .disc-face { padding-top: 54px; }
  .booking-title { font-size: 46px; line-height: 50px; margin-bottom: 6px; }
  .booking-detail { font-family: "Oswald", sans-serif; font-weight: 400; font-size: 16px; line-height: 30px; }
</style>
</head>
<body>
<main class="poster">
  <svg class="backdrop" width="1200" height="850" viewBox="0 0 1200 850" aria-hidden="true">
    <defs>
      <linearGradient id="band-light" x1="0" y1="0" x2="1" y2="0">
        <stop offset="0" stop-color="#2a2a2a"/>
        <stop offset="0.5" stop-color="#555555"/>
        <stop offset="1" stop-color="#1a1a1a"/>
      </linearGradient>
      <linearGradient id="band-dark" x1="0" y1="0" x2="1" y2="1">
        <stop offset="0" stop-color="#111111"/>
        <stop offset="0.6" stop-color="#3a3a3a"/>
        <stop offset="1" stop-color="#0a0a0a"/>
      </linearGradient>
    </defs>
    <path d="M0 430 C 300 380, 700 520, 1200 650 L1200 850 L0 850 Z" fill="url(#band-dark)"/>
    <path d="M0 520 C 350 470, 750 640, 1200 760 L1200 850 L0 850 Z" fill="#151515"/>
    <path d="M0 600 C 400 560, 800 700, 1200 800 L1200 810 C 800 720, 400 585, 0 625 Z" fill="url(#band-light)"/>
    <path d="M0 700 C 380 660, 760 780, 1200 850 L0 850 Z" fill="#0c0c0c"/>
  </svg>

  <h1 class="studio-name">Harwood Strength Studio</h1>
  <p class="tagline">Boutique personal and small group training studio</p>

  <section class="services">
    <h2 class="services-title">Personal training</h2>
    <p class="services-sub">Group fitness classes</p>
  </section>

  <ul class="class-list">
    <li class="class-item"><span class="class-icon yoga" role="img" aria-label="Yoga icon"></span><span class="class-label">Yoga</span></li>
    <li class="class-item"><span class="class-icon mma" role="img" aria-label="MMA icon"></span><span class="class-label">MMA conditioning</span></li>
    <li class="class-item"><span class="class-icon strength" role="img" aria-label="Strength icon"></span><span class="class-label">Strength circuit</span></li>
    <li class="class-item"><span class="class-icon body" role="img" aria-label="Body composition icon"></span><span class="class-label">Body composition analysis</span></li>
    <li class="class-item"><span class="class-icon nutrition" role="img" aria-label="Nutrition icon"></span><span class="class-label">Nutrition advice</span></li>
    <li class="class-item"><span class="class-icon osteo" role="img" aria-label="Osteopathy icon"></span><span class="class-label">Osteopathy</span></li>
  </ul>

  <div class="disc offer-disc">
    <div class="disc-face">
      <p class="offer-title">August special</p>
      <p class="offer-line first">all group fitness</p>
      <p class="offer-line second">classes <span class="offer-price">$10</span></p>
      <div class="offer-shoes" role="img" aria-label="Pair of running shoes"></div>
    </div>
  </div>

  <div class="disc booking-disc">
    <div class="disc-face">
      <p class="booking-title">Book online</p>
      <p class="booking-detail">www.harwoodstrengthstudio.com.au</p>
      <p class="booking-detail">or phone</p>
      <p class="booking-detail">0412 555 019</p>
      <p class="booking-detail">4/18 Mill Lane&nbsp; Harwood</p>
    </div>
  </div>
</main>
</body>
</html>
```